Online Bed Retailer needs a home page banner.

I need a web banner for the home page to my bed & mattress retail website.(www.slumbercratehub.com) I wish to communicate to the general public my offer of FREE UK delivery with every order & interest FREE credit with all orders over £350.

Industry/Entity Type

Retail

```html
<!DOCTYPE html>
<html lang="en">
<head>
<meta charset="utf-8">
<title>Free Credit &amp; Free UK Delivery Banner</title>
<link rel="stylesheet" href="https://fonts.googleapis.com/css2?family=Montserrat:ital,wght@0,900;1,500&family=Barlow:wght@500;700&display=swap">
<style>
  :root {
    --paper: #ffffff;
    --ink: #000000;
    --offer-blue: #0b56a6;
    --offer-outline: #2626b8;
    --band-blue: #0a55a5;
    --delivery-red: #e81c24;
    --text-light: #ffffff;
  }
  * { margin: 0; padding: 0; box-sizing: border-box; }
  html, body { width: 1200px; height: 1000px; overflow: hidden; background: var(--paper); }
  .canvas { position: relative; width: 1200px; height: 1000px; }
  .crop-marks { position: absolute; inset: 0; }
  .banner {
    position: absolute; left: 38px; top: 322px; width: 1124px; height: 356px;
    overflow: hidden; background: var(--paper);
  }
  .hero-photo {
    position: absolute; left: 0; top: 0; width: 700px; height: 283px;
    background:
      linear-gradient(90deg, rgba(255,255,255,0) 0%, rgba(255,255,255,0) 72%, #ffffff 100%),
      linear-gradient(100deg, #7a3a4a 0%, #b89a86 18%, #5a3fc0 34%, #c9b8a8 55%, #e6e2e0 80%);
  }
  .credit-headline {
    position: absolute; left: 0; top: 0; width: 1124px; height: 200px;
    font-family: "Montserrat", sans-serif; font-weight: 900;
  }
  .credit-headline span {
    position: absolute; line-height: 1; white-space: nowrap;
    color: var(--offer-blue);
    text-shadow:
      2px 0 0 var(--offer-outline), -2px 0 0 var(--offer-outline),
      0 2px 0 var(--offer-outline), 0 -2px 0 var(--offer-outline),
      1.5px 1.5px 0 var(--offer-outline), -1.5px -1.5px 0 var(--offer-outline),
      1.5px -1.5px 0 var(--offer-outline), -1.5px 1.5px 0 var(--offer-outline);
  }
  .credit-zero { left: 592px; top: 11px; font-size: 200px; letter-spacing: -4px; }
  .credit-free { left: 728px; top: 28px; font-size: 92px; letter-spacing: -1px; }
  .credit-word { left: 758px; top: 102px; font-size: 88px; letter-spacing: -2px; }
  .credit-band { position: absolute; left: 612px; top: 198px; }
  .credit-terms {
    position: absolute; left: 652px; top: 200px; width: 460px; height: 58px;
    font-family: "Montserrat", sans-serif; font-style: italic; font-weight: 500;
    font-size: 40px; line-height: 58px; color: var(--text-light); white-space: nowrap;
  }
  .delivery-band {
    position: absolute; left: 0; top: 283px; width: 1124px; height: 73px;
    background: var(--delivery-red); color: var(--text-light);
    font-family: "Barlow", sans-serif; font-weight: 500; font-size: 62px;
    letter-spacing: 3px; line-height: 73px; text-align: center; white-space: nowrap;
  }
  .delivery-band strong { font-weight: 700; }
</style>
</head>
<body>
<div class="canvas">
  <svg class="crop-marks" width="1200" height="1000" viewBox="0 0 1200 1000" aria-hidden="true">
    <g stroke="var(--ink)" stroke-width="1">
      <line x1="38.5" y1="292" x2="38.5" y2="314"/>
      <line x1="1161.5" y1="292" x2="1161.5" y2="314"/>
      <line x1="38.5" y1="686" x2="38.5" y2="708"/>
      <line x1="1161.5" y1="686" x2="1161.5" y2="708"/>
      <line x1="9" y1="322.5" x2="31" y2="322.5"/>
      <line x1="1169" y1="322.5" x2="1191" y2="322.5"/>
      <line x1="9" y1="677.5" x2="31" y2="677.5"/>
      <line x1="1169" y1="677.5" x2="1191" y2="677.5"/>
    </g>
  </svg>

  <section class="banner">
    <div class="hero-photo" role="img" aria-label="Delivery driver in a purple cap and polo unloading a plastic-wrapped mattress from a van full of beds"></div>

    <h1 class="credit-headline" aria-label="0% free credit">
      <span class="credit-zero">0</span>
      <span class="credit-free">% FREE</span>
      <span class="credit-word">CREDIT</span>
    </h1>

    <svg class="credit-band" width="512" height="58" viewBox="0 0 512 58" aria-hidden="true">
      <polygon points="38,0 512,0 512,58 0,58" fill="var(--band-blue)"/>
    </svg>
    <p class="credit-terms">on all order over £350</p>

    <p class="delivery-band"><strong>FREE</strong> UK DELIVERY ON ALL ORDERS</p>
  </section>
</div>
</body>
</html>
```